Holistic Psychologist needs contemporary business card

I am a psychologist working with adult clients face to face and online. The card needs to work for clients and also referring doctors and medical professionals. It needs to look warm, safe and trustable for clients, but clean and professional enough for doctors. Sometimes I also work in a corporate context.

I am holistic in my approach (mind-body-spirit) so anything conveying connection or integration or wholeness would be good. But again, clean and contemporary please. It can have a little bit of personality.
New logo uploaded.

Probably warm tones and plenty white space to write on one side.

My web pages:
http://mkcounsel.com.au
https://www.facebook.com/MarionKellerCounselling?ref=hl
Updates

Hi Designers .. I have decided I do need a new logo before finalising a design for the business cards.  I hope to have this available in 4 days from now.

Kindly,

Marion

New logo now posted, same brief.  Balance of masculine and feminine elements, plenty of white space on one side please.

Keen to see some card designs, thank-you.

Target Market(s)

Audience 1 - Males and females aged 25 years + seeking counselling or coaching. Audience 2 - doctors and health professionals who refer clients.

Industry/Entity Type

Medical

Contact Information for Business Card

Logo

Marion Keller
Registered Psychologist

M: 0491 582 034
www.mkcounsel.com.au
marion@mkcounsel.com.au
Little blue Facebook icon, with "marion keller counselling" printed near it.

Font styles to use
Sans Serif

Requirements
Nice to have
• You might want to play with the words "Balanced Self"
Should not have
• Nothing cutesy or too literal

```html
<!DOCTYPE html>
<html lang="en">
<head>
<meta charset="utf-8">
<title>Marion Keller Psychology – Business Card</title>
<link rel="stylesheet" href="https://fonts.googleapis.com/css2?family=Questrial&family=Arimo:wght@400&display=swap">
<style>
  :root {
    --backdrop: #b3b3b3;
    --card: #ffffff;
    --brand-red: #e31e24;
    --ink: #1a1a1a;
    --band-text: #ffffff;
    --faint-mark: #f7d3c4;
    --shadow: rgba(0, 0, 0, 0.22);
  }
  * { box-sizing: border-box; margin: 0; padding: 0; }
  html, body { width: 1200px; height: 900px; overflow: hidden; }
  body {
    background: var(--backdrop);
    position: relative;
    font-family: "Arimo", Arial, sans-serif;
    color: var(--ink);
  }
  .card {
    position: absolute;
    top: 290px;
    width: 540px;
    height: 320px;
    background: var(--card);
    border-radius: 22px;
    box-shadow: 0 14px 30px var(--shadow);
    overflow: hidden;
  }
  .card--front { left: 40px; }
  .card--back { left: 620px; }

  /* Front */
  .brand {
    position: absolute;
    left: 38px;
    top: 72px;
    display: flex;
    align-items: center;
    gap: 18px;
  }
  .brand__dot {
    width: 52px;
    height: 52px;
    border-radius: 50%;
    background: var(--brand-red);
    flex: none;
  }
  .brand__name {
    font-family: "Questrial", sans-serif;
    font-size: 40px;
    line-height: 1;
    color: var(--brand-red);
    white-space: nowrap;
  }
  .brand__practice {
    font-family: "Questrial", sans-serif;
    font-size: 19px;
    letter-spacing: 0.62em;
    color: var(--ink);
    margin-top: 8px;
    white-space: nowrap;
  }
  .tagline-band {
    position: absolute;
    left: 0;
    right: 0;
    top: 168px;
    height: 20px;
    background: var(--brand-red);
    display: flex;
    justify-content: space-between;
    align-items: center;
    padding: 0 50px;
    font-family: "Questrial", sans-serif;
    font-size: 13px;
    color: var(--band-text);
  }
  .contact-list {
    position: absolute;
    left: 28px;
    top: 208px;
    list-style: none;
    font-size: 16px;
    line-height: 23px;
  }
  .contact-list li { display: flex; align-items: center; gap: 5px; white-space: nowrap; }
  .contact-list svg { width: 16px; height: 16px; flex: none; }
  .social-square {
    width: 14px;
    height: 14px;
    margin: 0 1px;
    background: var(--brand-red);
    border-radius: 2px;
    flex: none;
  }

  /* Back */
  .back-mark {
    position: absolute;
    inset: 0;
    display: flex;
    align-items: center;
    justify-content: center;
    font-family: "Questrial", sans-serif;
    font-size: 76px;
    color: var(--faint-mark);
    white-space: nowrap;
  }
</style>
</head>
<body>

<section class="card card--front" aria-label="Card front">
  <div class="brand">
    <span class="brand__dot"></span>
    <div>
      <div class="brand__name">Marion Keller</div>
      <div class="brand__practice">PSYCHOLOGY</div>
    </div>
  </div>

  <div class="tagline-band" aria-label="Balanced Self">
    <span>B</span><span>A</span><span>L</span><span>A</span><span>N</span><span>C</span><span>E</span><span>D</span>
    <span>&nbsp;</span><span>&nbsp;</span>
    <span>S</span><span>E</span><span>L</span><span>F</span>
  </div>

  <ul class="contact-list">
    <li>
      <svg viewBox="0 0 16 16" aria-hidden="true"><rect x="4" y="1" width="8" height="14" rx="1.5" fill="var(--brand-red)"/><rect x="5.5" y="3" width="5" height="5" fill="#fff"/><rect x="5.5" y="9.5" width="5" height="3.5" fill="#fff" opacity=".6"/></svg>
      <span>0491 582 034</span>
    </li>
    <li>
      <svg viewBox="0 0 16 16" aria-hidden="true"><g fill="none" stroke="var(--brand-red)" stroke-width="1.4"><circle cx="8" cy="8" r="6.5"/><ellipse cx="8" cy="8" rx="3" ry="6.5"/><line x1="1.5" y1="8" x2="14.5" y2="8"/><line x1="2.5" y1="4.5" x2="13.5" y2="4.5"/><line x1="2.5" y1="11.5" x2="13.5" y2="11.5"/></g></svg>
      <span>www.mkcounsel.com.au</span>
    </li>
    <li>
      <svg viewBox="0 0 16 16" aria-hidden="true"><rect x="1" y="3.5" width="14" height="10" rx="1" fill="var(--brand-red)"/><path d="M1.5 4 L8 9 L14.5 4" fill="none" stroke="#fff" stroke-width="1.3"/></svg>
      <span>marion@mkcounsel.com.au</span>
    </li>
    <li>
      <span class="social-square"></span>
      <span>marion keller counselling</span>
    </li>
  </ul>
</section>

<section class="card card--back" aria-label="Card back">
  <div class="back-mark">Marion Keller</div>
</section>

</body>
</html>
```